bRm Design Group - architect web site

need a web site to permit potential clients to view our portfolio of work.

Will need lots of photos included.

Industry/Entity Type

Architect

Coding

Coded - Design and coding required

Number of Pages Required

5+ page

Font styles to use
Sans Serif

Requirements
Must have
• photos should be organized by project - perhaps a summary of photos and then click to enlarge? should be simple to operate. should be able to separate interior design from architecture.
• needs to be easy to add more photos in the future.

```html
<!DOCTYPE html>
<html lang="en">
<head>
<meta charset="utf-8">
<title>bRm Design Group</title>
<link rel="stylesheet" href="https://fonts.googleapis.com/css2?family=Lato:wght@300;400;700;900&display=swap">
<style>
  :root {
    --sky-deep: #163f70;
    --sky-mid: #2a5f98;
    --sky-light: #6f9cc9;
    --ink: #222222;
    --text: #444444;
    --white: #ffffff;
    --caption-bg: rgba(40, 40, 40, 0.72);
    --footer-bg: #474747;
    --footer-text: #d8d8d8;
    --accent-orange: #e8672b;
    --accent-green: #6aa842;
  }
  * { box-sizing: border-box; margin: 0; padding: 0; }
  html, body { width: 1200px; height: 2330px; overflow: hidden; }
  body { position: relative; background: var(--white); font-family: 'Lato', sans-serif; color: var(--text); }

  /* Hero */
  .hero {
    position: absolute; left: 0; top: 0; width: 1200px; height: 498px;
    background:
      radial-gradient(ellipse 520px 300px at 360px 120px, rgba(205, 215, 225, 0.55) 0%, rgba(205, 215, 225, 0) 70%),
      radial-gradient(ellipse 420px 240px at 860px 360px, rgba(190, 200, 210, 0.45) 0%, rgba(190, 200, 210, 0) 70%),
      linear-gradient(165deg, var(--sky-light) 0%, var(--sky-mid) 42%, var(--sky-deep) 100%);
  }
  .site-nav { position: absolute; left: 0; top: 0; width: 1200px; height: 40px; font-size: 11px; font-weight: 700; color: var(--white); }
  .site-nav span { position: absolute; top: 13px; }
  .site-nav .nav-brand { left: 366px; top: 8px; font-size: 15px; font-weight: 900; }
  .hero-brand { position: absolute; left: 0; top: 190px; width: 1200px; text-align: center; color: var(--white); }
  .hero-brand .brand-name { font-size: 80px; font-weight: 900; letter-spacing: 1px; line-height: 1; }
  .hero-brand .brand-sub { font-size: 20px; font-weight: 400; letter-spacing: 3px; margin-top: 6px; }

  /* Welcome */
  .welcome-title {
    position: absolute; top: 575px; left: 0; width: 1200px; text-align: center;
    font-size: 22px; font-weight: 400; color: var(--ink); letter-spacing: 1px;
  }
  .welcome-text {
    position: absolute; top: 634px; left: 361px; width: 478px; text-align: center;
    font-size: 10px; line-height: 13px; color: var(--text);
  }

  /* Featured */
  .section-label { position: absolute; left: 0; width: 1200px; text-align: center; font-size: 11px; color: var(--ink); letter-spacing: 1px; }
  .featured-label { top: 788px; text-transform: uppercase; }
  .feature-tile { position: absolute; top: 846px; width: 203px; height: 214px; overflow: hidden; }
  .feature-tile .tile-caption {
    position: absolute; left: 0; bottom: 0; width: 100%; height: 26px; line-height: 26px;
    background: var(--caption-bg); color: var(--white); text-align: center;
    font-size: 9px; letter-spacing: 1px; text-transform: uppercase;
  }
  .tile-exterior {
    left: 277px;
    background:
      radial-gradient(ellipse 110px 70px at 110px 110px, rgba(238, 226, 170, 0.95) 0%, rgba(238, 226, 170, 0) 100%),
      linear-gradient(180deg, #2f62a8 0%, #6f96c8 35%, #c9c39a 55%, #5c7a3a 78%, #34502a 100%);
  }
  .tile-kitchen {
    left: 497px;
    background:
      radial-gradient(ellipse 80px 120px at 150px 80px, rgba(90, 130, 70, 0.7) 0%, rgba(90, 130, 70, 0) 100%),
      linear-gradient(120deg, #f2efe9 0%, #e0cdb0 40%, #c8a67a 65%, #8f7658 100%);
  }
  .tile-bathroom {
    left: 718px;
    background:
      radial-gradient(ellipse 60px 90px at 40px 80px, rgba(120, 160, 110, 0.55) 0%, rgba(120, 160, 110, 0) 100%),
      linear-gradient(180deg, #f6f7f7 0%, #e3e7e8 45%, #b9bebf 75%, #8d9192 100%);
  }

  /* Banner */
  .banner {
    position: absolute; left: 0; top: 1174px; width: 1200px; height: 446px;
    background:
      radial-gradient(ellipse 110px 150px at 540px 270px, rgba(250, 238, 200, 0.95) 0%, rgba(250, 238, 200, 0) 100%),
      radial-gradient(ellipse 300px 230px at 530px 230px, rgba(70, 100, 140, 0.9) 0%, rgba(70, 100, 140, 0) 100%),
      linear-gradient(180deg, #1f4f8e 0%, #3b70ad 40%, #6a92bf 62%, #4f6f58 78%, #3e6a2e 100%);
  }
  .banner-cut { position: absolute; left: 0; top: 1174px; width: 1200px; height: 446px; }
  .banner-title { position: absolute; left: 338px; top: 1428px; font-size: 36px; font-weight: 700; color: var(--white); }

  /* Master pieces */
  .master-label { top: 1674px; font-size: 15px; letter-spacing: 0; }
  .master-main {
    position: absolute; left: 287px; top: 1745px; width: 351px; height: 329px;
    background:
      radial-gradient(ellipse 150px 100px at 170px 170px, rgba(236, 226, 178, 0.95) 0%, rgba(236, 226, 178, 0) 100%),
      linear-gradient(180deg, #1d4a8c 0%, #4f7bb8 32%, #a9b9b8 50%, #c9c08e 62%, #4e6c30 80%, #2f4a22 100%);
  }
  .master-arrow {
    position: absolute; left: 618px; top: 1900px; width: 18px; height: 20px;
    background: var(--white); display: flex; align-items: center; justify-content: center;
  }
  .thumb-grid {
    position: absolute; left: 652px; top: 1743px; width: 264px;
    display: grid; grid-template-columns: repeat(6, 37px); grid-auto-rows: 29px; gap: 6px 7px;
  }
  .thumb { background: linear-gradient(180deg, #3a6aa8 0%, #cfc496 55%, #50693a 100%); }
  .thumb:nth-child(3n) { background: linear-gradient(135deg, #ece6dc 0%, #bfa27d 100%); }
  .thumb:nth-child(4n+1) { background: linear-gradient(135deg, #f1f2f2 0%, #a8adaf 100%); }
  .thumb:nth-child(5n+2) { background: linear-gradient(180deg, #1d3f70 0%, #476a94 60%, #2d4a2a 100%); }

  /* Footer */
  .site-footer { position: absolute; left: 0; top: 2165px; width: 1200px; height: 165px; background: var(--footer-bg); color: var(--footer-text); }
  .contact-block { position: absolute; top: 52px; display: flex; align-items: flex-start; gap: 10px; }
  .contact-icon { width: 30px; height: 30px; border-radius: 50%; display: flex; align-items: center; justify-content: center; margin-top: 4px; }
  .icon-phone { background: var(--accent-orange); }
  .icon-pin { background: var(--accent-green); }
  .contact-lines { font-size: 10px; line-height: 12px; }
  .contact-lines .contact-name { font-size: 15px; line-height: 18px; color: var(--white); }
  .contact-phone { left: 295px; }
  .contact-person { left: 479px; }
  .footer-company { position: absolute; left: 715px; top: 63px; font-size: 10px; }
  .footer-company strong { color: var(--white); font-weight: 700; letter-spacing: 1px; }
  .footer-copy { position: absolute; left: 0; top: 134px; width: 1200px; text-align: center; font-size: 8px; }
</style>
</head>
<body>

<header class="hero" role="img" aria-label="Photograph of a white steel pergola against a deep blue sky">
  <nav class="site-nav">
    <span class="nav-brand">bRm</span>
    <span style="left:570px">Portfolio</span>
    <span style="left:652px">Gallery</span>
    <span style="left:730px">About</span>
    <span style="left:805px">Contact</span>
  </nav>
  <div class="hero-brand">
    <div class="brand-name">bRm</div>
    <div class="brand-sub">DESIGN GROUP</div>
  </div>
</header>

<h1 class="welcome-title">WELCOME</h1>
<p class="welcome-text">bRm Design Group is a small studio of architects and interior designers creating homes, cottages and commercial spaces shaped by light, landscape and the way people live. From first sketch to final finish we guide every project with care, balancing classic island character with modern comfort. Browse our portfolio to see recent exterior, kitchen and bathroom work, and contact our team to begin planning a space that feels crafted for you.</p>

<h2 class="section-label featured-label">Featured Designs</h2>
<div class="feature-tile tile-exterior" role="img" aria-label="Photograph of a pale yellow two-storey house with white roof">
  <div class="tile-caption">Exterior Design</div>
</div>
<div class="feature-tile tile-kitchen" role="img" aria-label="Photograph of a bright kitchen with stone surfaces">
  <div class="tile-caption">Kitchen Design</div>
</div>
<div class="feature-tile tile-bathroom" role="img" aria-label="Photograph of a white bathroom with tub and vanity">
  <div class="tile-caption">Bathroom Design</div>
</div>

<div class="banner" role="img" aria-label="Photograph of an arched house entrance lit at dusk with ocean behind"></div>
<svg class="banner-cut" viewBox="0 0 1200 446" aria-hidden="true">
  <polygon points="0,324 1200,446 0,446" fill="#ffffff"/>
</svg>
<h2 class="banner-title">Crafted perfect</h2>

<h2 class="section-label master-label">Our Master piece</h2>
<div class="master-main" role="img" aria-label="Photograph of a yellow house with white roof and wooden porch"></div>
<div class="master-arrow">
  <svg width="8" height="10" viewBox="0 0 8 10" aria-hidden="true"><polyline points="2,1 6,5 2,9" fill="none" stroke="#333" stroke-width="1.6"/></svg>
</div>
<div class="thumb-grid" role="img" aria-label="Grid of small project photographs">
  <div class="thumb"></div><div class="thumb"></div><div class="thumb"></div><div class="thumb"></div><div class="thumb"></div><div class="thumb"></div>
  <div class="thumb"></div><div class="thumb"></div><div class="thumb"></div><div class="thumb"></div><div class="thumb"></div><div class="thumb"></div>
  <div class="thumb"></div><div class="thumb"></div><div class="thumb"></div><div class="thumb"></div><div class="thumb"></div><div class="thumb"></div>
  <div class="thumb"></div><div class="thumb"></div><div class="thumb"></div><div class="thumb"></div><div class="thumb"></div><div class="thumb"></div>
  <div class="thumb"></div><div class="thumb"></div><div class="thumb"></div><div class="thumb"></div><div class="thumb"></div><div class="thumb"></div>
  <div class="thumb"></div><div class="thumb"></div><div class="thumb"></div>
</div>

<footer class="site-footer">
  <div class="contact-block contact-phone">
    <div class="contact-icon icon-phone">
      <svg width="16" height="16" viewBox="0 0 24 24" aria-hidden="true"><path fill="#fff" d="M6.6 10.8c1.4 2.8 3.8 5.1 6.6 6.6l2.2-2.2c.3-.3.7-.4 1-.2 1.1.4 2.3.6 3.6.6.6 0 1 .4 1 1V20c0 .6-.4 1-1 1C10.6 21 3 13.4 3 4c0-.6.4-1 1-1h3.5c.6 0 1 .4 1 1 0 1.3.2 2.5.6 3.6.1.3 0 .7-.2 1z"/></svg>
    </div>
    <div class="contact-lines">
      <div>Call us today</div>
      <div>T 441 555 0142</div>
      <div>F 441 555 0143</div>
    </div>
  </div>
  <div class="contact-block contact-person">
    <div class="contact-icon icon-pin">
      <svg width="14" height="16" viewBox="0 0 24 24" aria-hidden="true"><path fill="#fff" d="M12 2C8.1 2 5 5.1 5 9c0 5.2 7 13 7 13s7-7.8 7-13c0-3.9-3.1-7-7-7zm0 9.5a2.5 2.5 0 1 1 0-5 2.5 2.5 0 0 1 0 5z"/></svg>
    </div>
    <div class="contact-lines">
      <div class="contact-name">Marcus Pellow</div>
      <div>Project Manager</div>
      <div>M 441 555 0187</div>
      <div>Hamilton, BM</div>
    </div>
  </div>
  <div class="footer-company"><strong>bRm DESIGN GROUP</strong> | hello@brmdesign.example</div>
  <div class="footer-copy">© 2024 bRm Design Group</div>
</footer>

</body>
</html>
```